Halloway Crest Backers Guild business cards

Create a single-sided business card for the Halloway Crest Backers Guild based on the attached logo.
The additional data fields include Name, Title, Email, Phone, and website.
Please use the following as sample data:
Name: Dean Varrow
Title: Co-Founder / Investor
Email: deanvarrow@mailtern.net
Phone: 555-314-2706
Website: www.hcbackersguild.com

Target Market(s)

Start ups, entrepreneurs, venture capitalists

Industry/Entity Type

Investment

Contact Information for Business Card

Professional business card. Technology company.

Font styles to use
Serif
Sans Serif

Requirements
Must have
• Include the HCBG logo (attached)
• Name
• Title
• Email
• Phone
• Website
Should not have
• Cute, cartoony

```html
<!DOCTYPE html>
<html lang="en">
<head>
<meta charset="utf-8">
<title>Halloway Crest Backers Guild – Business Card</title>
<link href="https://fonts.googleapis.com/css2?family=Open+Sans:wght@400;600&display=swap" rel="stylesheet">
<style>
  :root {
    --backdrop: #e9e6e1;
    --card: #ffffff;
    --ink: #231f20;
    --green: #16964a;
    --shadow: rgba(0, 0, 0, 0.14);
  }
  html, body {
    margin: 0;
    padding: 0;
    width: 1200px;
    height: 801px;
    overflow: hidden;
    background: var(--backdrop);
    font-family: "Open Sans", Arial, sans-serif;
  }
  .stage {
    width: 1200px;
    height: 801px;
    display: flex;
    align-items: center;
    justify-content: center;
  }
  .card {
    position: relative;
    width: 980px;
    height: 560px;
    background: var(--card);
    box-shadow: 0 10px 30px var(--shadow);
    box-sizing: border-box;
  }
  .brand {
    position: absolute;
    left: 96px;
    top: 176px;
    display: flex;
    align-items: center;
    gap: 22px;
  }
  .brand-mark {
    width: 58px;
    height: 58px;
    background: var(--green);
    flex: none;
  }
  .brand-name {
    margin: 0;
    color: var(--green);
    font-weight: 600;
    font-size: 30px;
    line-height: 1.2;
    letter-spacing: 0.5px;
  }
  .contact {
    position: absolute;
    left: 560px;
    top: 236px;
  }
  .person-name {
    margin: 0;
    color: var(--ink);
    font-weight: 600;
    font-size: 38px;
    line-height: 1.1;
  }
  .person-title {
    margin: 4px 0 18px;
    color: var(--green);
    font-weight: 400;
    font-size: 21px;
  }
  .details {
    list-style: none;
    margin: 0;
    padding: 0;
  }
  .details li {
    display: flex;
    align-items: center;
    gap: 14px;
    color: var(--ink);
    font-size: 21px;
    line-height: 1.7;
  }
  .details svg {
    width: 20px;
    height: 20px;
    flex: none;
    fill: var(--green);
  }
</style>
</head>
<body>
<main class="stage">
  <section class="card">
    <div class="brand">
      <div class="brand-mark"></div>
      <p class="brand-name">Halloway Crest<br>Backers Guild</p>
    </div>
    <div class="contact">
      <h1 class="person-name">Dean Varrow</h1>
      <p class="person-title">Co-Founder / Investor</p>
      <ul class="details">
        <li>
          <svg viewBox="0 0 20 20" aria-hidden="true"><path d="M1 4h18v12H1z M2.5 5.5 10 11l7.5-5.5" fill="var(--green)" stroke="#fff" stroke-width="1.2"/></svg>
          deanvarrow@mailtern.net
        </li>
        <li>
          <svg viewBox="0 0 20 20" aria-hidden="true"><path d="M3 6c0-2 2-3 7-3s7 1 7 3v1h-4V5.5H7V7H3z M4 9h12l1 7H3z"/><circle cx="10" cy="12.5" r="2" fill="#fff"/></svg>
          555-314-2706
        </li>
        <li>
          <svg viewBox="0 0 20 20" aria-hidden="true"><g fill="none" stroke="var(--green)" stroke-width="1.4"><circle cx="10" cy="10" r="8"/><ellipse cx="10" cy="10" rx="3.5" ry="8"/><path d="M2 10h16M3.5 6h13M3.5 14h13"/></g></svg>
          www.hcbackersguild.com
        </li>
      </ul>
    </div>
  </section>
</main>
</body>
</html>
```